Bright Path Flyer Design for Virtual Online Clinic. -5.5 x 8.5 inches (half sheet)

We need a clean, modern flyer design for Bright Path, a new virtual walk-in clinic based in British Columbia. The flyer will be used in libraries, pharmacies, and community centers to help residents easily access primary care through their Bright Path NFC access card.
The flyer will ask a question : NEED A DOCTOR? This should be large and attention grabbing.
The design should clearly feature a Bright Path card image (the access card) as the centerpiece and visually show how patients can use it to book appointments. The tone should feel trustworthy, healthcare-oriented, and community-friendly — clean fonts, clear spacing, and strong readability from a distance.

Side One: This card has the NFC Access Card.
NEED A DOCTOR? (Large Font, Attention Grabbing)
How to Book an Appointment using your Bright Path Card
Step 1: Tap Your Card on Your Phone
Hold your card near the back of your phone.
It will activate automatically — no app needed.
The Bright Path scheduler will open.
Step 2: Schedule Your Appointment
Select your clinical concern.
Choose your time window.
Register (only once).
Confirm your appointment.
Step 3: Relax, we’ll take care of the rest
A doctor will call during your scheduled time.
Once booked, you’ll be able to call our office.
No emails, no texts — just a real person.
It’s that simple.
Side Two:
About Bright Path
Created by Dr. Marcus Ferrigan
Bright Path was founded to make healthcare simple and convenient. Prescription renewals. Common infections. Medical notes. And so much more.
Our doctors can address 120+ health concerns virtually — providing quality care without the waiting room. No waiting rooms. Just real doctors providing real care.
Why Patients Choose Bright Path
Easy access – book and be seen from anywhere in BC.
Effortless booking – tap your Bright Path Card to begin.
Trusted physicians – every visit is with a licensed BC family doctor.
How It Works
Book your visit — choose a time window that fits your day.
Join the queue — you’ll be called when it’s your turn.
Speak directly with your doctor — simple, secure, and stress-free.
Convenient Care for Common Concerns

Additional Details.
Please find the domain to be launched soon. I've attached the NFC card file for review, it is 85.5 mm x 54 mm. The card will be glued to the flyer.
I've attached examples of flyers but they are not the look I am seeking and I am looking for creative solutions.
Thank you!
http://brightpath-example.test/

Adult Patients in British Columbia

Healthcare

• Looking for clean lines, uniform appearance, and high legibility i.e poppins

0054AA
0677BA
7BADD7
CADEEF
E8F1F8

• Need A Doctor?
• Elegant style, not too busy, clear layout.
• Clutter, look cheap - review examples.

```html
<!DOCTYPE html>
<html lang="en">
<head>
<meta charset="UTF-8">
<title>About Bright Path</title>
<link href="https://fonts.googleapis.com/css2?family=Poppins:wght@500;600;700&display=swap" rel="stylesheet">
<style>
  :root {
    --navy: #0054AA;
    --deep-navy: #0a3d8f;
    --ocean: #0677BA;
    --sky: #3aaed4;
    --pill: #3db3dc;
    --mist: #E8F1F8;
    --green: #18b57c;
    --ink: #1d1d2b;
    --white: #ffffff;
  }
  * { margin: 0; padding: 0; box-sizing: border-box; }
  html, body { width: 846px; height: 1200px; overflow: hidden; }
  body { font-family: "Poppins", sans-serif; background: var(--white); }
  .flyer {
    position: relative;
    width: 846px;
    height: 1200px;
    background: linear-gradient(180deg, #f4f8fc 0%, var(--mist) 100%);
    overflow: hidden;
  }
  .brand-bar {
    position: absolute; top: 0; left: 0; width: 100%; height: 109px;
    background: var(--white);
    display: flex; align-items: center; justify-content: center;
  }
  .brand-name {
    font-weight: 600; font-size: 42px; color: var(--deep-navy);
    letter-spacing: 0.5px;
  }
  .hero {
    position: absolute; top: 109px; left: 0; width: 100%; height: 464px;
    background: linear-gradient(90deg, var(--navy) 0%, var(--ocean) 55%, var(--sky) 100%);
  }
  .hero-title {
    position: absolute; top: 74px; width: 100%; text-align: center;
    color: var(--white); font-weight: 700; font-size: 60px;
    line-height: 70px; letter-spacing: 3px;
  }
  .creator-pill {
    position: absolute; top: 280px; left: 207px; width: 433px; height: 107px;
    border-radius: 54px; background: var(--pill);
    display: flex; flex-direction: column; align-items: center; justify-content: center;
    color: var(--white); text-align: center;
  }
  .creator-label { font-weight: 600; font-size: 22px; letter-spacing: 1.5px; line-height: 28px; }
  .creator-name { font-weight: 700; font-size: 28px; letter-spacing: 1.5px; line-height: 36px; }
  .intro {
    position: absolute; top: 600px; left: 40px; width: 766px;
    text-align: center; color: var(--ink);
    font-weight: 500; font-size: 20.5px; line-height: 24px; letter-spacing: 0.6px;
  }
  .section-bar {
    position: absolute; left: 51px; width: 746px; height: 52px;
    background: var(--green); border-radius: 10px;
    display: flex; align-items: center; justify-content: center;
    color: var(--white); font-weight: 600; font-size: 37px; letter-spacing: 0.3px;
  }
  .section-bar.why { top: 785px; }
  .section-bar.how { top: 958px; }
  .point-list {
    position: absolute; left: 55px; width: 760px; list-style: none;
    color: #2a2a35; font-weight: 500; font-size: 19px; line-height: 24px; letter-spacing: 0.5px;
  }
  .point-list.why { top: 858px; }
  .point-list.how { top: 1029px; left: 62px; font-weight: 600; }
  .footer-rule {
    position: absolute; top: 1160px; left: 64px; width: 490px; height: 2px;
    background: var(--deep-navy);
  }
  .site-pill {
    position: absolute; top: 1143px; left: 551px; width: 237px; height: 35px;
    border-radius: 18px; background: var(--deep-navy);
    border: 2px solid #7BADD7;
    display: flex; align-items: center; justify-content: center;
    color: var(--white); font-weight: 600; font-size: 12.5px;
  }
</style>
</head>
<body>
  <main class="flyer">
    <header class="brand-bar">
      <span class="brand-name">Bright Path</span>
    </header>

    <section class="hero">
      <h1 class="hero-title">ABOUT<br>BRIGHT PATH</h1>
      <div class="creator-pill">
        <span class="creator-label">CREATED BY:</span>
        <span class="creator-name">DR. MARCUS FERRIGAN</span>
      </div>
    </section>

    <p class="intro">Bright Path was founded to make healthcare simple and convenient. Prescription renewals. Common infections. Medical notes. And so much more.<br>Our doctors can address 120+ health concerns virtually — providing quality care without the waiting room. No waiting rooms. Just real doctors providing real care.</p>

    <h2 class="section-bar why">Why Patients Choose Bright Path</h2>
    <ul class="point-list why">
      <li>Easy access – book and be seen from anywhere in BC.</li>
      <li>Effortless booking – tap your Bright Path Card to begin.</li>
      <li>Trusted physicians – every visit is with a licensed BC family doctor.</li>
    </ul>

    <h2 class="section-bar how">How It Works</h2>
    <ul class="point-list how">
      <li>Book your visit — choose a time window that fits your day.</li>
      <li>Join the queue — you’ll be called when it’s your turn.</li>
      <li>Speak directly with your doctor — simple, secure, and stress-free.</li>
      <li>Convenient Care for Common Concerns.</li>
    </ul>

    <div class="footer-rule"></div>
    <div class="site-pill">http://brightpath-example.test/</div>
  </main>
</body>
</html>
```